Tech Startup Needs Business Card Design

I am looking for an eye catching business card design for our new company, Torn Kite. We are a place for business owners and contractors to share their experiences with their customers and check their current customers. Our website, www.torn-kite.co, may be able to offer some guidance as to the design.

Industry/Entity Type

Business

Contact Information for Business Card

Owen Barthwick
888-417-3083
Owen@torn-kite.co
www.torn-kite.co

```html
<!DOCTYPE html>
<html lang="en">
<head>
<meta charset="utf-8">
<title>Torn Kite — Business Card</title>
<link rel="stylesheet" href="https://fonts.googleapis.com/css2?family=Nunito:wght@800&family=Questrial&display=swap">
<style>
  :root {
    --page-bg: #d9e0df;
    --ink-dark: #1b1c1e;
    --brand-red: #f20f0f;
    --brand-red-deep: #c30202;
    --brand-red-fold: #8b0000;
    --paper: #eef0f0;
    --paper-shade: #dfe2e2;
    --white: #ffffff;
  }
  * { margin: 0; padding: 0; box-sizing: border-box; }
  html, body { width: 1200px; height: 1200px; overflow: hidden; background: var(--page-bg); }
  .canvas { position: relative; width: 1200px; height: 1200px; }
  .card {
    position: absolute; left: 150px; width: 900px; height: 514px;
    overflow: hidden; box-shadow: 0 6px 18px rgba(0,0,0,0.18);
  }
  .card--front { top: 60px; }
  .card--back { top: 626px; }
  .card__art { position: absolute; inset: 0; width: 900px; height: 514px; display: block; }

  .holder-name {
    position: absolute; left: 52px; top: 268px;
    font-family: "Nunito", sans-serif; font-weight: 800; font-size: 44px;
    color: var(--white); transform: rotate(-3.5deg); transform-origin: left center;
  }
  .contact-list { position: absolute; left: 80px; top: 396px; list-style: none; }
  .contact-list__item {
    display: flex; align-items: center; gap: 14px; height: 36px;
    font-family: "Questrial", sans-serif; font-size: 18px; color: var(--white);
  }
  .contact-list__icon { width: 30px; height: 30px; flex: none; }

  .brand-lockup {
    position: absolute; display: flex; flex-direction: column; align-items: center; gap: 18px;
    font-family: "Questrial", sans-serif; color: var(--brand-red); white-space: nowrap;
  }
  .brand-lockup__dot { border-radius: 50%; background: var(--brand-red); }
  .brand-lockup--front { left: 470px; top: 140px; width: 330px; font-size: 66px; }
  .brand-lockup--front .brand-lockup__dot { width: 120px; height: 120px; }
  .brand-lockup--back { left: 300px; top: 160px; width: 300px; font-size: 48px; gap: 14px; }
  .brand-lockup--back .brand-lockup__dot { width: 90px; height: 90px; }
</style>
</head>
<body>
<main class="canvas">

  <section class="card card--front" aria-label="Business card front">
    <svg class="card__art" viewBox="0 0 900 514" aria-hidden="true">
      <defs>
        <linearGradient id="paperGrad" x1="0" y1="0" x2="0" y2="1">
          <stop offset="0" stop-color="var(--paper)"/>
          <stop offset="1" stop-color="var(--paper-shade)"/>
        </linearGradient>
        <linearGradient id="bandGrad" x1="0" y1="0" x2="0" y2="1">
          <stop offset="0" stop-color="#d90000"/>
          <stop offset="1" stop-color="#ff1010"/>
        </linearGradient>
      </defs>
      <rect width="900" height="514" fill="url(#paperGrad)"/>
      <polygon points="0,0 400,0 320,200 440,310 490,514 0,514" fill="var(--ink-dark)"/>
      <polygon points="330,170 440,215 320,225" fill="var(--brand-red-fold)"/>
      <polygon points="440,305 360,335 410,390" fill="var(--brand-red-fold)"/>
      <polygon points="0,240 440,212 440,310 0,392" fill="url(#bandGrad)"/>
      <rect x="840" y="222" width="26" height="110" fill="var(--brand-red)"/>
      <polygon points="875,215 900,212 900,325 875,328" fill="var(--brand-red)"/>
      <polygon points="600,514 690,455 900,430 900,514" fill="var(--brand-red)"/>
    </svg>

    <div class="brand-lockup brand-lockup--front">
      <span class="brand-lockup__dot"></span>
      <span class="brand-lockup__name">Torn Kite</span>
    </div>

    <p class="holder-name">Owen Barthwick</p>

    <ul class="contact-list">
      <li class="contact-list__item">
        <svg class="contact-list__icon" viewBox="0 0 30 30" aria-hidden="true">
          <circle cx="15" cy="15" r="15" fill="var(--brand-red)"/>
          <path d="M10 8 l3 0 l1.5 4 l-2 1.5 a9 9 0 0 0 4 4 l1.5 -2 l4 1.5 l0 3 a2 2 0 0 1 -2 2 a13 13 0 0 1 -12 -12 a2 2 0 0 1 2 -2z" fill="var(--white)"/>
        </svg>
        <span>888-417-3083</span>
      </li>
      <li class="contact-list__item">
        <svg class="contact-list__icon" viewBox="0 0 30 30" aria-hidden="true">
          <circle cx="15" cy="15" r="15" fill="var(--brand-red)"/>
          <rect x="7.5" y="10" width="15" height="10" fill="var(--white)"/>
          <path d="M7.5 10 L15 16 L22.5 10" fill="none" stroke="var(--brand-red)" stroke-width="1.5"/>
        </svg>
        <span>Owen@torn-kite.co</span>
      </li>
      <li class="contact-list__item">
        <svg class="contact-list__icon" viewBox="0 0 30 30" aria-hidden="true">
          <circle cx="15" cy="15" r="15" fill="var(--brand-red)"/>
          <g fill="none" stroke="var(--white)" stroke-width="1.4">
            <circle cx="15" cy="15" r="8"/>
            <ellipse cx="15" cy="15" rx="3.5" ry="8"/>
            <line x1="7" y1="15" x2="23" y2="15"/>
            <line x1="8.5" y1="11" x2="21.5" y2="11"/>
            <line x1="8.5" y1="19" x2="21.5" y2="19"/>
          </g>
        </svg>
        <span>www.torn-kite.co</span>
      </li>
    </ul>
  </section>

  <section class="card card--back" aria-label="Business card back">
    <svg class="card__art" viewBox="0 0 900 514" aria-hidden="true">
      <rect width="900" height="514" fill="var(--brand-red)"/>
      <polygon points="450,270 900,120 900,514 440,514" fill="var(--brand-red-deep)"/>
      <polygon points="0,0 900,0 900,60 450,200 0,40" fill="var(--brand-red-fold)"/>
      <polygon points="0,40 450,200 0,300" fill="var(--brand-red)"/>
      <polygon points="450,200 900,60 900,120 450,270" fill="var(--brand-red-deep)"/>
      <polygon points="450,70 625,170 625,370 450,470 275,370 275,170" fill="var(--brand-red-fold)"/>
      <polygon points="450,70 625,170 450,105 275,170" fill="var(--brand-red)"/>
      <polygon points="450,105 595,188 595,352 450,435 305,352 305,188" fill="var(--white)"/>
    </svg>

    <div class="brand-lockup brand-lockup--back">
      <span class="brand-lockup__dot"></span>
      <span class="brand-lockup__name">Torn Kite</span>
    </div>
  </section>

</main>
</body>
</html>
```